Business Card Design Project

We need a business card design for a new company based in New York called "Kestrel Co's". Efficient lighting for large spaces: we plan and install LED systems built to save energy. We would like a double sided card with our contact info on one side with our logo (to be designed) and on the other side the services we provide. We would like a heavy weight glossy card using the colors green and white. The final design should communicate environmental soundness and our market is very upscale corporations.
We would like our logo to illustrate LED lighting and we were thinking if we could get a stock picture of the Calloway Spire Tower lit up on July 4th with red, white and blue LED lighting. The alternative would be anything that connotes environmentally proper thinking. It could be either a picture or a design.

```html
<!DOCTYPE html>
<html lang="en">
<head>
<meta charset="utf-8">
<title>Kestrel Co's — Business Card</title>
<link rel="stylesheet" href="https://fonts.googleapis.com/css2?family=Arimo:ital,wght@0,400;0,700;1,400&display=swap">
<style>
  :root {
    --bg: #e9ebe6;
    --green-deep: #4f9a1e;
    --green-mid: #7cc43a;
    --green-light: #b9ea6a;
    --green-text: #6cb52d;
    --white: #ffffff;
    --paper: #f3f4f2;
    --ink: #1b1b1b;
    --navy: #2b2f8c;
    --shadow: rgba(30, 40, 20, 0.22);
  }
  * { box-sizing: border-box; margin: 0; padding: 0; }
  html, body { width: 1200px; height: 872px; overflow: hidden; }
  body {
    background: var(--bg);
    font-family: "Arimo", Arial, sans-serif;
    position: relative;
  }

  .card {
    position: absolute;
    width: 560px;
    height: 320px;
    border-radius: 4px;
    box-shadow: 0 10px 28px var(--shadow);
    overflow: hidden;
  }

  /* Front: services side */
  .card-front {
    left: 70px;
    top: 60px;
    background:
      radial-gradient(ellipse 60% 55% at 55% 45%, var(--green-light) 0%, rgba(185,234,106,0) 70%),
      linear-gradient(160deg, var(--green-mid) 0%, var(--green-deep) 100%);
    color: var(--white);
    text-align: center;
  }
  .front-brand {
    position: absolute;
    top: 58px;
    left: 0;
    right: 0;
    display: flex;
    flex-direction: column;
    align-items: center;
    gap: 14px;
  }
  .brand-dot {
    width: 54px;
    height: 54px;
    border-radius: 50%;
    background: var(--green-deep);
  }
  .card-front .brand-dot { background: var(--white); opacity: 0.85; }
  .card-front .brand-name {
    font-size: 44px;
    font-weight: 400;
    color: var(--green-deep);
    letter-spacing: 1px;
  }
  .front-tagline {
    position: absolute;
    left: 30px;
    right: 30px;
    top: 212px;
    font-size: 21px;
    line-height: 1.3;
    letter-spacing: 0.5px;
  }

  /* Back: contact side */
  .card-back {
    left: 260px;
    top: 410px;
    background: linear-gradient(170deg, var(--white) 0%, var(--paper) 100%);
    color: var(--ink);
  }
  .back-brand {
    position: absolute;
    left: 40px;
    top: 26px;
    display: flex;
    align-items: center;
    gap: 10px;
  }
  .back-brand .brand-dot { width: 26px; height: 26px; background: var(--green-text); }
  .back-brand .brand-name { font-size: 22px; color: var(--green-text); }
  .back-watermark {
    position: absolute;
    right: 70px;
    top: 40px;
    width: 170px;
    height: 170px;
    border-radius: 50%;
    background: var(--green-text);
    opacity: 0.08;
  }
  .holder {
    position: absolute;
    left: 24px;
    top: 112px;
    border-left: 10px solid var(--navy);
    padding: 2px 0 2px 14px;
  }
  .holder-name { font-size: 19px; color: var(--green-text); }
  .holder-role { font-size: 15px; color: var(--green-text); margin-top: 2px; }
  .contacts {
    position: absolute;
    left: 44px;
    top: 200px;
    display: grid;
    grid-template-columns: 62px auto;
    row-gap: 3px;
    font-size: 14px;
  }
  .contacts dt { color: var(--green-text); font-style: italic; }
  .address {
    position: absolute;
    left: 300px;
    top: 222px;
    width: 236px;
    font-size: 14px;
    line-height: 1.35;
  }
  .address-label { color: var(--green-text); font-style: italic; margin-bottom: 4px; }

  /* Standalone brand lockup */
  .lockup {
    position: absolute;
    right: 60px;
    bottom: 56px;
    display: flex;
    align-items: center;
    gap: 20px;
  }
  .lockup .brand-dot { width: 70px; height: 70px; background: var(--green-text); }
  .lockup .brand-name {
    font-size: 66px;
    color: var(--green-text);
    letter-spacing: 2px;
  }
</style>
</head>
<body>

  <section class="card card-front" aria-label="Card front: services">
    <div class="front-brand">
      <span class="brand-dot"></span>
      <span class="brand-name">Kestrel Co's</span>
    </div>
    <p class="front-tagline">“Efficient lighting for large spaces: we plan and install LED systems built to save energy.”</p>
  </section>

  <section class="card card-back" aria-label="Card back: contact details">
    <div class="back-brand">
      <span class="brand-dot"></span>
      <span class="brand-name">Kestrel Co's</span>
    </div>
    <span class="back-watermark"></span>
    <div class="holder">
      <p class="holder-name">Dana Whitfield</p>
      <p class="holder-role">Designer</p>
    </div>
    <dl class="contacts">
      <dt>Phone:</dt><dd>212 555 0148</dd>
      <dt>Mail:</dt><dd>dana@kestrelco.com</dd>
      <dt>Web:</dt><dd>www.kestrelco.com</dd>
    </dl>
    <div class="address">
      <p class="address-label">Address:</p>
      <p>48 Harbor Lane, Suite 210,<br>New York, NY 10001</p>
    </div>
  </section>

  <div class="lockup">
    <span class="brand-dot"></span>
    <span class="brand-name">Kestrel Co's</span>
  </div>

</body>
</html>
```